Re-branding for Structural Engineering firm

We need new business cards as part of our current re-branding. We have a new logo (attached), so the card design should incorporate this color scheme. We are a structural engineering firm providing structural building design and seismic consulting services. The final design should communicate professionalism and stability, with a modern look and feel.

```html
<!DOCTYPE html>
<html lang="en">
<head>
<meta charset="utf-8">
<title>Halvern Structural Engineering – Business Card</title>
<link href="https://fonts.googleapis.com/css2?family=Source+Sans+3:wght@400;600;700&display=swap" rel="stylesheet">
<style>
  :root {
    --page-bg: #6f7c88;
    --navy: #111a28;
    --navy-deep: #16294a;
    --slate: #2a2a36;
    --blue: #1f6fb8;
    --blue-dark: #165a9a;
    --ink: #1c4a86;
    --grey: #9a9a9a;
    --white: #ffffff;
  }
  html, body {
    margin: 0;
    width: 1200px;
    height: 1200px;
    overflow: hidden;
    background: var(--page-bg);
    font-family: "Source Sans 3", "Myriad Pro", sans-serif;
  }
  .card {
    position: absolute;
    left: 75px;
    top: 300px;
    width: 1050px;
    height: 600px;
    background: var(--white);
    overflow: hidden;
    box-shadow: 0 14px 30px rgba(0,0,0,.35);
  }
  .card-art {
    position: absolute;
    inset: 0;
  }
  .brand {
    position: absolute;
    left: 80px;
    top: 150px;
    display: flex;
    align-items: flex-start;
    gap: 18px;
  }
  .brand-square {
    width: 40px;
    height: 40px;
    background: var(--blue);
    margin-top: 6px;
  }
  .brand-name {
    color: var(--grey);
    font-weight: 600;
    font-size: 34px;
    line-height: 1.05;
    letter-spacing: 1px;
    text-transform: uppercase;
  }
  .brand-name .line { display: block; }
  .holder {
    position: absolute;
    left: 610px;
    top: 58px;
    color: var(--ink);
  }
  .holder-name {
    margin: 0;
    font-size: 46px;
    font-weight: 700;
    line-height: 1;
  }
  .holder-title {
    margin: 4px 0 0 150px;
    font-size: 28px;
    font-weight: 700;
  }
  .contact-list {
    position: absolute;
    left: 588px;
    top: 250px;
    margin: 0;
    padding: 0;
    list-style: none;
    color: var(--ink);
    font-size: 25px;
    line-height: 1.15;
  }
  .contact-list li {
    height: 56px;
    display: flex;
    align-items: center;
  }
  .contact-list li.address { height: 70px; }
</style>
</head>
<body>
  <div class="card">
    <svg class="card-art" width="1050" height="600" viewBox="0 0 1050 600">
      <polygon points="0,0 470,0 560,120 560,600 0,600" fill="var(--blue)"/>
      <polygon points="420,40 470,40 545,110 505,130" fill="var(--blue-dark)"/>
      <polygon points="0,0 400,0 505,130 505,600 0,600" fill="var(--navy)"/>
      <rect x="80" y="420" width="330" height="180" fill="var(--navy-deep)"/>
      <rect x="250" y="380" width="170" height="220" fill="var(--slate)"/>

      <g fill="var(--navy)">
        <circle cx="515" cy="285" r="24"/>
        <circle cx="515" cy="348" r="24"/>
        <circle cx="515" cy="404" r="24"/>
        <circle cx="515" cy="460" r="24"/>
        <circle cx="515" cy="516" r="24"/>
      </g>
      <g fill="var(--white)" stroke="none">
        <path d="M515 272 a9 9 0 0 1 9 9 c0 7 -9 16 -9 16 s-9 -9 -9 -16 a9 9 0 0 1 9 -9z"/>
        <circle cx="515" cy="281" r="3.5" fill="var(--navy)"/>
        <path d="M505 340 l5 -3 4 7 -3 3 c2 4 4 6 8 8 l3 -3 7 4 -3 5 c-12 0 -21 -9 -21 -21z"/>
        <rect x="503" y="400" width="24" height="14" rx="2"/>
        <path d="M501 400 c4 -8 24 -8 28 0 l-5 2 c-3 -4 -15 -4 -18 0z"/>
        <circle cx="515" cy="407" r="4" fill="var(--navy)"/>
      </g>
      <g fill="none" stroke="var(--white)" stroke-width="2">
        <rect x="503" y="452" width="24" height="16" rx="1"/>
        <path d="M503 453 l12 9 12 -9"/>
        <circle cx="515" cy="516" r="12"/>
        <ellipse cx="515" cy="516" rx="5" ry="12"/>
        <path d="M503 516 h24"/>
      </g>
    </svg>

    <div class="brand">
      <span class="brand-square"></span>
      <span class="brand-name">
        <span class="line">Halvern</span>
        <span class="line">Structural</span>
        <span class="line">Engineering</span>
      </span>
    </div>

    <div class="holder">
      <h1 class="holder-name">Lena Marwick, S.E.</h1>
      <div class="holder-title">Principal</div>
    </div>

    <ul class="contact-list">
      <li class="address">4170 Harbor Ridge Dr., Ste 210<br>Coastview, CA 92070</li>
      <li>555.284.6190</li>
      <li>555.731.4028</li>
      <li>lena@halvernse.com</li>
      <li>www.halvernse.com</li>
    </ul>
  </div>
</body>
</html>
```